Sex trafficking Survivors Brochure ********

I need a general brochure for a new non-profit committed to empowering survivors of sexual exploitation. I kept the wording to a minimum so the design will help me tell the story. The brochure will be used in churches and other venues when I give presentations. I will also be using this in one on one presentations to walk through the highlights of our work. We are in the aftercare business and the feel should communicate hope and new beginnings.

I would like a single fold brochure- about 8.5x5.5.
Updates

to clarify- the brochure should be 8.5 by 5.5 Added Wednesday, November 05, 2014

Target Market(s)

donors, volunteers- all ages- mainly women

Industry/Entity Type

Non-Profit

Font styles to use
Serif

Requirements
Must have
• Pictures draw me in. I tend to like professional designs with just enough color and detail to make them unique.
• Hopeful- note the picture I attached are bright- not sad and depressed. Feel free to add your own photos if they are better. My favorite picture is the black woman with sun.
• Please use a variety of races- we serve a diverse population.
• I also need my website listed www.brightharborhome.org
Nice to have
• I have seen some designs that use one picture to stretch across the front and back of the brochure. This might be interesting if it works, but I may have too much text on the back to make this worthwhile.
Should not have
• hearts, country feel, goofy, whimsical

```html
<!DOCTYPE html>
<html lang="en">
<head>
<meta charset="utf-8">
<title>Bright Harbor Brochure</title>
<link href="https://fonts.googleapis.com/css2?family=Crimson+Text:wght@400;700&family=Quicksand:wght@400;500&display=swap" rel="stylesheet">
<style>
  :root {
    --bg: #2b2b2b;
    --paper: #ffffff;
    --sky: #5cb4e4;
    --sky-soft: rgba(92, 170, 222, 0.82);
    --royal: #1f5fb3;
    --navy: #1c2f5a;
    --ink: #222222;
    --sun: #ffe100;
    --rule: #5cb4e4;
  }
  * { margin: 0; padding: 0; box-sizing: border-box; }
  html, body { width: 1200px; height: 900px; overflow: hidden; background: var(--bg); }
  body { position: relative; font-family: "Crimson Text", Georgia, serif; color: var(--ink); }

  .spread { position: absolute; left: 50px; top: 40px; width: 1100px; height: 356px; background: var(--paper); }
  .page { position: absolute; top: 0; width: 550px; height: 356px; overflow: hidden; }
  .page--left { left: 0; }
  .page--right { left: 550px; border-left: 1px solid #e3e3e3; }

  .photo { position: absolute; }
  .heading { font-family: "Quicksand", Arial, sans-serif; font-weight: 400; color: var(--sky); }
  .body-copy { font-size: 9.5px; line-height: 1.2; }

  /* left page */
  .photo--cafe { left: 0; top: 0; width: 215px; height: 150px; background: linear-gradient(135deg, #c9b9a2, #8d6e64 45%, #d7d3cb); }
  .photo--portrait { left: 215px; top: 0; width: 335px; height: 356px; background: linear-gradient(90deg, #d9dde0 0 40px, #4e6b3a 40px, #88a36b 45%, #a77d5c 70%, #8aa4c0); }
  .intro { position: absolute; left: 0; top: 150px; width: 215px; height: 206px; background: var(--paper); padding: 20px 18px 0 22px; }
  .intro__block { padding-bottom: 7px; margin-bottom: 10px; border-bottom: 1px solid var(--rule); }
  .intro__block .heading { font-size: 20px; line-height: 1; margin-bottom: 3px; }
  .brand-mark { position: absolute; left: 22px; bottom: 14px; display: flex; align-items: center; gap: 6px; font-size: 10px; color: var(--royal); }
  .brand-mark__dot { width: 14px; height: 14px; border-radius: 50%; background: var(--royal); }

  .model { position: absolute; left: 235px; top: 140px; width: 315px; height: 216px; background: var(--sky-soft); padding: 12px 16px 0 16px; color: #1d2b3a; }
  .model .heading { color: #ffffff; font-size: 20px; line-height: 1.1; margin-bottom: 8px; }
  .model__item { margin-bottom: 9px; }
  .tag { display: inline-block; font-weight: 700; font-size: 9.5px; line-height: 13px; padding: 0 14px 0 5px; border-radius: 0 7px 7px 0; margin-bottom: 2px; }
  .tag--light { background: #ffffff; color: var(--royal); }
  .tag--blue { background: var(--sky); color: #ffffff; }

  /* right page */
  .sky-block { position: absolute; left: 0; top: 0; width: 300px; height: 100px; background: linear-gradient(90deg, var(--sky), #9fd3f0); }
  .roles { position: absolute; left: 22px; top: 108px; width: 262px; }
  .roles .heading { font-size: 20px; line-height: 1.1; margin-bottom: 8px; }
  .roles__item { margin-bottom: 7px; }
  .side { position: absolute; left: 300px; top: 0; width: 250px; height: 356px; }
  .photo--friends { left: 0; top: 0; width: 250px; height: 140px; background: linear-gradient(120deg, #d9cbb8, #5b3d32 50%, #c8b8a8); }
  .web-band { position: absolute; left: 0; top: 140px; width: 250px; height: 90px; background: var(--royal); }
  .photo--talk { left: 10px; top: 10px; width: 100px; height: 70px; background: linear-gradient(135deg, #d6a0a6, #6a4c48 55%, #b9c3cf); }
  .web-band__url { position: absolute; right: 10px; top: 54px; font-family: "Quicksand", Arial, sans-serif; font-size: 8.5px; color: #ffffff; white-space: nowrap; }
  .photo--library { left: 0; top: 230px; width: 250px; height: 126px; background: linear-gradient(90deg, #8a5a3a, #c79a6a 40%, #3d2a22 70%, #d8d2c8); }

  /* cover */
  .cover { position: absolute; left: 320px; top: 440px; width: 560px; height: 362px; overflow: hidden; }
  .photo--cover { left: 0; top: 0; width: 560px; height: 362px; background: radial-gradient(circle at 22% 15%, #fffbe8 0, #f3e2b0 18%, transparent 40%), linear-gradient(90deg, #b89a72, #a4553e 50%, #d9c7a8 80%, #e9dccb); }
  .cover__brand { position: absolute; left: 22px; top: 16px; display: flex; align-items: center; gap: 8px; font-size: 20px; color: var(--navy); letter-spacing: 1px; }
  .cover__brand-dot { width: 30px; height: 30px; border-radius: 50%; background: var(--royal); }
  .sun-band { position: absolute; left: 0; top: 252px; width: 560px; height: 110px; background: rgba(255, 225, 0, 0.86); }
  .tagline { position: absolute; right: 40px; top: 14px; font-family: "Quicksand", Arial, sans-serif; color: var(--royal); line-height: 0.95; }
  .tagline__big { display: block; font-size: 32px; }
  .tagline__mid { display: block; font-size: 24px; padding-left: 28px; font-weight: 500; }
</style>
</head>
<body>

<section class="spread">
  <div class="page page--left">
    <div class="photo photo--cafe" role="img" aria-label="Photo of three friends laughing together at an outdoor cafe"></div>
    <div class="photo photo--portrait" role="img" aria-label="Photo of a smiling young woman with curly hair in a plaid shirt outdoors"></div>

    <div class="intro">
      <div class="intro__block">
        <h2 class="heading">Vision</h2>
        <p class="body-copy">Survivors of sexual exploitation live free, fulfilling their God-given purpose.</p>
      </div>
      <div class="intro__block">
        <h2 class="heading">Mission</h2>
        <p class="body-copy">Mobilize communities to encourage and equip survivors of sexual exploitation to build new lives.</p>
      </div>
      <div class="brand-mark"><span class="brand-mark__dot"></span>Bright Harbor</div>
    </div>

    <div class="model">
      <h2 class="heading">Our Model</h2>
      <div class="model__item">
        <span class="tag tag--light">Heal</span>
        <p class="body-copy">Survivors need safe relationships and a safe environment to heal. Bright Harbor facilitates mentor relationships, offers a supportive community and immerses survivors in faith-based curriculum.</p>
      </div>
      <div class="model__item">
        <span class="tag tag--light">Discover</span>
        <p class="body-copy">In order to thrive, survivors need to discover their innate ability, preferences, personality and spiritual gifts.</p>
      </div>
      <div class="model__item">
        <span class="tag tag--light">Overcome</span>
        <p class="body-copy">Survivors overcome barriers to moving ahead with the right educational and employment options.</p>
      </div>
    </div>
  </div>

  <div class="page page--right">
    <div class="sky-block"></div>
    <div class="roles">
      <h2 class="heading">Your Role</h2>
      <div class="roles__item">
        <span class="tag tag--blue">Mentor</span>
        <p class="body-copy">Build a safe nurturing relationship with one woman and encourage her to reach her goals. Join a community who receive training and support to effectively mentor.</p>
      </div>
      <div class="roles__item">
        <span class="tag tag--blue">Teacher</span>
        <p class="body-copy">Teach group classes on life skills, biblical studies, physical wellbeing, creative arts, conflict resolution, emotional health, literacy, and financial management.</p>
      </div>
      <div class="roles__item">
        <span class="tag tag--blue">Business Partner</span>
        <p class="body-copy">Provide employment and business coaching to a survivor.</p>
      </div>
      <div class="roles__item">
        <span class="tag tag--blue">Supporter</span>
        <p class="body-copy">Financially and prayerfully support the work of Bright Harbor.</p>
      </div>
    </div>

    <div class="side">
      <div class="photo photo--friends" role="img" aria-label="Photo of two smiling young women side by side"></div>
      <div class="web-band">
        <div class="photo photo--talk" role="img" aria-label="Photo of two women in a close conversation"></div>
        <span class="web-band__url">www.brightharborhome.org</span>
      </div>
      <div class="photo photo--library" role="img" aria-label="Photo of a young woman studying in a library with books"></div>
    </div>
  </div>
</section>

<section class="cover">
  <div class="photo photo--cover" role="img" aria-label="Photo of a woman with a headband raising her hand toward the sun in front of a brick building"></div>
  <div class="cover__brand"><span class="cover__brand-dot"></span>BRIGHT HARBOR</div>
  <div class="sun-band">
    <p class="tagline">
      <span class="tagline__big">Where</span>
      <span class="tagline__mid">true freedom</span>
      <span class="tagline__big">begins</span>
    </p>
  </div>
</section>

</body>
</html>
```